Velora Autohaus Nordic
Velora Autohaus Nordic - Automotive
Creative Brief
Modern
Velora Autohaus Nordic Oy
Автомобили и мототехника из США и Европы
info@veloraautohaus.example
www.veloraautohaus.example
The data that I would like to see: Velora Autohaus Nordic Oy Автомобили и мототехника из США и Европы (Cars and bikes from the U.S. and Europe) Контакты Phone: +7-918-647-20-83 (mobile phone) Skype: veloraautohaus Email: info@veloraautohaus.example www.veloraautohaus.example Генеральный директор (Director general) Белянский Артём Феликсович
On consideration of the developer. Will consider any options.

```html
<!DOCTYPE html>
<html lang="ru">
<head>
<meta charset="utf-8">
<title>Velora Autohaus Nordic — Stationery</title>
<link rel="stylesheet" href="https://fonts.googleapis.com/css2?family=PT+Sans:wght@400;700&display=swap">
<style>
  :root {
    --stage-dark: #02050d;
    --stage-glow: #0b2a66;
    --brand-deep: #06207a;
    --brand-blue: #1658e0;
    --brand-light: #7fb6ff;
    --paper: #ffffff;
    --ink: #1a1f2c;
    --ink-soft: #4a5160;
    --label: #c9d3e6;
    --window-line: #c9ced8;
  }
  * { margin: 0; padding: 0; box-sizing: border-box; }
  html, body { width: 1200px; height: 826px; overflow: hidden; }
  body {
    position: relative;
    font-family: "PT Sans", Arial, sans-serif;
    color: var(--ink);
    background:
      radial-gradient(ellipse 520px 420px at 330px 520px, rgba(30,90,200,0.55), transparent 70%),
      radial-gradient(ellipse 700px 500px at 860px 330px, rgba(20,60,150,0.35), transparent 70%),
      var(--stage-dark);
  }
  .piece-label {
    position: absolute;
    font-size: 12px;
    color: var(--label);
    letter-spacing: 0.02em;
  }
  .label-envelope { left: 326px; top: 38px; }
  .label-card-front { left: 72px; top: 502px; }
  .label-card-back { left: 72px; top: 685px; }
  .label-letterhead { left: 820px; top: 673px; }

  .brand-name {
    font-family: "PT Sans", Arial, sans-serif;
    font-weight: 400;
    text-transform: uppercase;
    letter-spacing: 0.02em;
    white-space: nowrap;
    line-height: 1;
  }
  .brand-tagline { white-space: nowrap; letter-spacing: 0.03em; }

  .contacts { font-size: 8px; line-height: 1.45; color: var(--ink); }
  .contacts .contacts-title { font-weight: 700; font-size: 8.5px; }
  .contacts .field { display: inline-block; width: 38px; }

  /* Envelope */
  .envelope { position: absolute; left: 120px; top: 67px; width: 485px; }
  .envelope-flap { display: block; }
  .envelope-body {
    position: relative;
    width: 485px; height: 240px;
    background: linear-gradient(168deg, var(--brand-deep) 0%, var(--brand-blue) 12%, #5e9cff 24%, #cfe3ff 36%, var(--paper) 48%);
  }
  .envelope-body .brand-name { position: absolute; left: 30px; top: 18px; font-size: 25px; color: var(--paper); }
  .envelope-body .brand-tagline { position: absolute; left: 31px; top: 46px; font-size: 9px; color: #dce9ff; }
  .envelope-window {
    position: absolute; left: 30px; top: 88px; width: 190px; height: 78px;
    border: 1px solid var(--window-line); border-radius: 6px; background: var(--paper);
  }
  .envelope-body .contacts { position: absolute; left: 30px; top: 178px; }
  .envelope-body .site { position: absolute; left: 30px; top: 224px; font-size: 8px; font-weight: 700; }

  /* Business cards */
  .card {
    position: absolute; left: 216px; width: 276px; height: 168px; border-radius: 10px; overflow: hidden;
  }
  .card-front {
    top: 420px;
    background: linear-gradient(100deg, #0a3fb8 0%, var(--brand-blue) 35%, #5aa0ff 70%, #9fcbff 100%);
    box-shadow: 0 0 18px rgba(60,130,255,0.35);
  }
  .card-front .brand-name { position: absolute; left: 14px; top: 18px; font-size: 20px; color: var(--paper); }
  .card-front .brand-tagline { position: absolute; left: 15px; top: 40px; font-size: 7.5px; color: #e2edff; }
  .card-front .person { position: absolute; left: 62px; top: 60px; color: var(--paper); }
  .card-front .person-name { font-size: 7.5px; font-weight: 700; }
  .card-front .person-role { font-size: 7px; }
  .card-front .contacts { position: absolute; left: 96px; top: 88px; color: var(--paper); font-size: 7px; }
  .card-front .site { position: absolute; left: 0; right: 0; top: 138px; text-align: center; font-size: 7.5px; color: var(--paper); }

  .card-back {
    top: 605px;
    background:
      linear-gradient(125deg, rgba(10,30,90,0.9) 0%, rgba(20,70,190,0.75) 45%, rgba(6,18,60,0.95) 80%);
    border: 1px solid rgba(120,170,255,0.35);
  }
  .card-back .brand-name { position: absolute; left: 14px; top: 24px; font-size: 20px; color: var(--paper); }
  .card-back .brand-tagline { position: absolute; left: 15px; top: 46px; font-size: 7.5px; color: #cfe0ff; }

  /* Letterhead */
  .letterhead {
    position: absolute; left: 660px; top: 43px; width: 396px; height: 617px; overflow: hidden;
    background: linear-gradient(152deg, var(--brand-deep) 0%, var(--brand-blue) 10%, #5d9bff 18%, #cfe2ff 26%, var(--paper) 34%);
  }
  .letterhead-mark {
    position: absolute; left: 40px; top: 260px;
    transform: rotate(-24deg); transform-origin: left top;
    color: rgba(30,50,90,0.06);
  }
  .letterhead-mark .brand-name { font-size: 30px; }
  .letterhead-mark .brand-tagline { font-size: 11px; }
  .letterhead .contacts { position: absolute; left: 40px; top: 478px; }
  .letterhead .site { position: absolute; left: 40px; top: 556px; font-size: 8px; font-weight: 700; }
</style>
</head>
<body>

  <p class="piece-label label-envelope">ENVELOPE</p>

  <section class="envelope">
    <svg class="envelope-flap" width="485" height="77" viewBox="0 0 485 77">
      <defs>
        <linearGradient id="flapFill" x1="0" y1="0" x2="1" y2="0.3">
          <stop offset="0" stop-color="#041a66"/>
          <stop offset="0.55" stop-color="#0f45c4"/>
          <stop offset="0.8" stop-color="#0a2a8a"/>
          <stop offset="1" stop-color="#020a2a"/>
        </linearGradient>
      </defs>
      <polygon points="0,77 6,0 479,0 485,77" fill="url(#flapFill)"/>
      <g transform="rotate(180 242 40)" fill="#ffffff" font-family="PT Sans, Arial, sans-serif">
        <text x="242" y="58" text-anchor="middle" font-size="19" letter-spacing="0.5">VELORA AUTOHAUS NORDIC</text>
        <text x="242" y="70" text-anchor="middle" font-size="8" fill="#cfe0ff">Автомобили и мототехника из США и Европы</text>
      </g>
    </svg>
    <div class="envelope-body">
      <p class="brand-name">Velora Autohaus Nordic</p>
      <p class="brand-tagline">Автомобили и мототехника из США и Европы</p>
      <div class="envelope-window"></div>
      <div class="contacts">
        <p class="contacts-title">Контакты</p>
        <p><span class="field">Mobile :</span>+7-918-647-20-83</p>
        <p><span class="field">Skype :</span>veloraautohaus</p>
        <p><span class="field">Email :</span>info@veloraautohaus.example</p>
      </div>
      <p class="site">www.veloraautohaus.example</p>
    </div>
  </section>

  <p class="piece-label label-card-front">Business Card - FRONT</p>
  <section class="card card-front">
    <p class="brand-name">Velora Autohaus Nordic</p>
    <p class="brand-tagline">Автомобили и мототехника из США и Европы</p>
    <div class="person">
      <p class="person-name">Белянский Артём Феликсович</p>
      <p class="person-role">Генеральный директор</p>
    </div>
    <div class="contacts">
      <p class="contacts-title">Контакты</p>
      <p><span class="field">Mobile :</span>+7-918-647-20-83</p>
      <p><span class="field">Skype :</span>veloraautohaus</p>
      <p><span class="field">Email :</span>info@veloraautohaus.example</p>
    </div>
    <p class="site">www.veloraautohaus.example</p>
  </section>

  <p class="piece-label label-card-back">Business Card - BACK</p>
  <section class="card card-back">
    <p class="brand-name">Velora Autohaus Nordic</p>
    <p class="brand-tagline">Автомобили и мототехника из США и Европы</p>
  </section>

  <section class="letterhead">
    <div class="letterhead-mark" aria-hidden="true">
      <p class="brand-name">Velora Autohaus Nordic</p>
      <p class="brand-tagline">Автомобили и мототехника из США и Европы</p>
    </div>
    <div class="contacts">
      <p class="contacts-title">Контакты</p>
      <p><span class="field">Mobile :</span>+7-918-647-20-83</p>
      <p><span class="field">Skype :</span>veloraautohaus</p>
      <p><span class="field">Email :</span>info@veloraautohaus.example</p>
    </div>
    <p class="site">www.veloraautohaus.example</p>
  </section>
  <p class="piece-label label-letterhead">Letterhead sheet</p>

</body>
</html>
```